Business cards for a tribute and obituary website

Our website is called Quiet Orchard.

It is a special place online for people to remember their loved ones who have passed away, through obituaries and tributes. Friends and family can also convey their condolences on the deceased's memorial page. Celebrating the life of the deceased and remembering their legacy is very important to us – death should not be just about grieving.

We would like the card to look tasteful and modern. The design should ideally not have colours that are too bright. The logo and website URL, www.quietorchardpages.net should be visible on the front of the card, with our slogan "Celebrating a life passed" on the back.

The design should communicate our purpose – remembering loved ones who have passed – and also a lighter tone of celebrating life. It should not look like a funeral director's card!

Our logo has been attached. Looking forward to some beautiful designs! Get creative :)
Updates

Reason: Thank you all for your designs. The rest of my team and I have not reached a decision on which design to select and I am collecting feedback from them. I will provide feedback for any changes that need to be made soon. It would be great if we could see more original designs and in more colours! We will definitely select a design by this deadline.

Industry/Entity Type

Business

Contact Information for Business Card

Nadia Fenwick
Project Manager
471226809
nadiafenwick@quietorchardpages.net

Font styles to use
Serif
Sans Serif

Requirements
Must have
• Logo and website address (www.quietorchardpages.net) on the front.
Nice to have
• Hi designers! It would be nice to see alternative colours – feel free to try out colours that are tasteful and subtle. The colour of the business card does not have to be the same as the logo.
• We would also like to see the logo used in different ways, perhaps a glossy or embossed finish. The card should look stylish.

```html
<!DOCTYPE html>
<html lang="en">
<head>
<meta charset="utf-8">
<title>Quiet Orchard – Business Card</title>
<link href="https://fonts.googleapis.com/css2?family=Roboto+Slab:wght@700&family=Exo+2:wght@400;500&display=swap" rel="stylesheet">
<style>
  :root {
    --backdrop: #2b2c2e;
    --navy: #0a2a4a;
    --band-dark: #5b5e62;
    --band-light: #8a8d91;
    --icon-disc: #c9cacc;
    --divider: #6e7480;
    --white: #ffffff;
  }
  html, body {
    margin: 0;
    padding: 0;
    width: 1200px;
    height: 817px;
    overflow: hidden;
    background: var(--backdrop);
  }
  .card {
    position: absolute;
    left: 100px;
    top: 123px;
    width: 1000px;
    height: 570px;
    background: var(--navy);
    border-radius: 40px;
    overflow: hidden;
    font-family: "Exo 2", sans-serif;
    color: var(--white);
  }
  .brand {
    position: absolute;
    left: 70px;
    top: 72px;
    display: flex;
    align-items: center;
    gap: 22px;
  }
  .brand-disc {
    width: 74px;
    height: 74px;
    border-radius: 50%;
    background: var(--white);
  }
  .brand-name {
    font-family: "Roboto Slab", serif;
    font-weight: 700;
    font-size: 50px;
    line-height: 0.95;
    color: var(--white);
  }
  .stripe {
    position: absolute;
    left: 0;
    right: 0;
    top: 222px;
    height: 52px;
    background: var(--band-dark);
  }
  .stripe-light {
    position: absolute;
    left: 0;
    top: 0;
    width: 470px;
    height: 100%;
    background: var(--band-light);
  }
  .holder {
    position: absolute;
    left: 40px;
    top: 0;
    height: 52px;
    display: flex;
    align-items: center;
    white-space: nowrap;
  }
  .person {
    width: 34px;
    height: 38px;
    margin-right: 18px;
  }
  .holder-name {
    font-size: 30px;
    letter-spacing: 1.5px;
  }
  .holder-sep {
    margin: 0 22px 0 52px;
    font-size: 30px;
  }
  .holder-role {
    font-size: 18px;
    letter-spacing: 1.5px;
  }
  .contact {
    position: absolute;
    top: 294px;
    width: 333px;
    height: 180px;
    text-align: center;
  }
  .contact--phone { left: 0; }
  .contact--mail { left: 333px; }
  .contact--web { left: 666px; }
  .contact-icon {
    display: block;
    margin: 8px auto 0;
    width: 72px;
    height: 72px;
  }
  .contact-text {
    margin-top: 34px;
    font-size: 28px;
    letter-spacing: 1px;
    white-space: nowrap;
  }
  .contact--mail .contact-text,
  .contact--web .contact-text {
    font-size: 16px;
    letter-spacing: 0.5px;
    margin-top: 40px;
  }
  .divider {
    position: absolute;
    top: 300px;
    width: 2px;
    height: 160px;
    background: var(--divider);
  }
  .divider--a { left: 333px; }
  .divider--b { left: 666px; }
  .band-address {
    position: absolute;
    left: 0;
    right: 0;
    top: 486px;
    height: 46px;
    background: var(--band-dark);
    display: flex;
    align-items: center;
    padding-left: 48px;
    gap: 18px;
    font-size: 19px;
    letter-spacing: 2px;
  }
  .pin { width: 20px; height: 28px; }
</style>
</head>
<body>
  <div class="card">
    <div class="brand">
      <div class="brand-disc"></div>
      <div class="brand-name">Quiet<br>Orchard</div>
    </div>

    <div class="stripe">
      <div class="stripe-light"></div>
      <div class="holder">
        <svg class="person" viewBox="0 0 36 40" aria-hidden="true">
          <circle cx="18" cy="11" r="9" fill="var(--white)"/>
          <path d="M2 40 Q2 22 18 22 Q34 22 34 40 Z" fill="var(--white)"/>
        </svg>
        <span class="holder-name">NADIA FENWICK</span>
        <span class="holder-sep">|</span>
        <span class="holder-role">PROJECT MANAGER</span>
      </div>
    </div>

    <div class="divider divider--a"></div>
    <div class="divider divider--b"></div>

    <div class="contact contact--phone">
      <svg class="contact-icon" viewBox="0 0 72 72" aria-hidden="true">
        <circle cx="36" cy="36" r="36" fill="var(--icon-disc)"/>
        <rect x="26" y="16" width="20" height="38" rx="4" fill="none" stroke="var(--navy)" stroke-width="3"/>
        <line x1="26" y1="22" x2="46" y2="22" stroke="var(--navy)" stroke-width="2"/>
        <line x1="26" y1="47" x2="46" y2="47" stroke="var(--navy)" stroke-width="2"/>
      </svg>
      <div class="contact-text">471 226 809</div>
    </div>

    <div class="contact contact--mail">
      <svg class="contact-icon" viewBox="0 0 72 72" aria-hidden="true">
        <circle cx="36" cy="36" r="36" fill="var(--icon-disc)"/>
        <rect x="18" y="24" width="36" height="24" fill="var(--navy)"/>
        <path d="M18 24 L36 38 L54 24" fill="none" stroke="var(--icon-disc)" stroke-width="2"/>
      </svg>
      <div class="contact-text">nadiafenwick@quietorchardpages.net</div>
    </div>

    <div class="contact contact--web">
      <svg class="contact-icon" viewBox="0 0 72 72" aria-hidden="true">
        <circle cx="36" cy="36" r="36" fill="var(--icon-disc)"/>
        <g fill="none" stroke="var(--navy)" stroke-width="2.5">
          <circle cx="36" cy="36" r="17"/>
          <ellipse cx="36" cy="36" rx="7" ry="17"/>
          <line x1="19" y1="36" x2="53" y2="36"/>
          <line x1="22" y1="27" x2="50" y2="27"/>
          <line x1="22" y1="45" x2="50" y2="45"/>
        </g>
      </svg>
      <div class="contact-text">www.quietorchardpages.net</div>
    </div>

    <div class="band-address">
      <svg class="pin" viewBox="0 0 20 28" aria-hidden="true">
        <path d="M10 0 C4 0 0 4.5 0 10 C0 17 10 28 10 28 C10 28 20 17 20 10 C20 4.5 16 0 10 0 Z" fill="var(--white)"/>
        <circle cx="10" cy="10" r="4" fill="var(--band-dark)"/>
      </svg>
      <span class="address">041.12th floor,Elm Crossing Road NRV</span>
    </div>
  </div>
</body>
</html>
```